CFO services graphic design

I own a business consulting firm called Hollins Advisory and we need a graphic for CFO services in our colours and branding. The attached file "CFO services to be put into Hollins advisory theme", shows the content for the design. The two other files show the theme and colours for the new design.

```html
<!DOCTYPE html>
<html lang="en">
<head>
<meta charset="UTF-8">
<title>Hollins Advisory – Chief Financial Officer Services</title>
<link href="https://fonts.googleapis.com/css2?family=Lato:wght@300;400;700;900&display=swap" rel="stylesheet">
<style>
  :root {
    --orange: #f7941d;
    --blue: #00aeef;
    --navy: #17378a;
    --ink: #0f2559;
    --panel: #ececec;
    --white: #ffffff;
  }
  html, body {
    margin: 0;
    padding: 0;
    width: 1200px;
    height: 927px;
    overflow: hidden;
    background: var(--white);
  }
  .sheet {
    position: relative;
    width: 1200px;
    height: 927px;
    background: var(--white);
    font-family: "Lato", sans-serif;
    color: var(--navy);
  }
  .brand {
    position: absolute;
    top: 74px;
    left: 0;
    width: 1200px;
    display: flex;
    justify-content: center;
    align-items: center;
    gap: 14px;
  }
  .brand-dot {
    width: 38px;
    height: 38px;
    border-radius: 50%;
    background: var(--orange);
  }
  .brand-name {
    font-family: "Lato", sans-serif;
    font-weight: 300;
    font-size: 36px;
    letter-spacing: 3px;
    color: var(--blue);
    text-transform: uppercase;
  }
  .panel {
    position: absolute;
    border-radius: 14px;
  }
  .panel--left { background: linear-gradient(to right, rgba(236,236,236,0), var(--panel) 70%); }
  .panel--right { background: linear-gradient(to left, rgba(236,236,236,0), var(--panel) 70%); }
  .diagram {
    position: absolute;
    left: 0;
    top: 0;
  }
  .service {
    position: absolute;
    font-weight: 700;
    font-size: 22.5px;
    line-height: 27px;
    color: var(--navy);
  }
  .service--left { text-align: right; }
  .service--right { text-align: left; }
  .service-detail {
    display: block;
    font-weight: 400;
    font-size: 18.5px;
    line-height: 23.5px;
  }
  .role-title {
    position: absolute;
    left: 453px;
    top: 330px;
    width: 300px;
    text-align: center;
    font-weight: 900;
    font-size: 38px;
    line-height: 40px;
    color: var(--ink);
    letter-spacing: 0.5px;
  }
  .footer-band {
    position: absolute;
    left: 0;
    top: 841px;
    width: 1165px;
    height: 55px;
    background: var(--blue);
    display: flex;
    align-items: center;
  }
  .footer-accent {
    position: absolute;
    left: 1165px;
    top: 841px;
    width: 35px;
    height: 55px;
    background: var(--orange);
  }
  .web-icon { margin-left: 66px; margin-right: 12px; }
  .web-address {
    color: var(--white);
    font-size: 25px;
    letter-spacing: 7.5px;
    font-weight: 400;
  }
</style>
</head>
<body>
<div class="sheet">

  <div class="brand">
    <span class="brand-dot"></span>
    <span class="brand-name">Hollins Advisory</span>
  </div>

  <!-- text panels -->
  <div class="panel panel--left" style="left:36px;top:195px;width:312px;height:146px;"></div>
  <div class="panel panel--left" style="left:36px;top:362px;width:283px;height:133px;"></div>
  <div class="panel panel--left" style="left:74px;top:514px;width:311px;height:126px;"></div>
  <div class="panel panel--left" style="left:203px;top:674px;width:311px;height:126px;"></div>
  <div class="panel panel--right" style="left:678px;top:674px;width:311px;height:126px;"></div>
  <div class="panel panel--right" style="left:813px;top:514px;width:295px;height:126px;"></div>
  <div class="panel panel--right" style="left:876px;top:362px;width:261px;height:133px;"></div>
  <div class="panel panel--right" style="left:850px;top:195px;width:287px;height:146px;"></div>

  <svg class="diagram" width="1200" height="927" viewBox="0 0 1200 927">
    <!-- orbit -->
    <path d="M440 302 A182 182 0 1 0 760 302" fill="none" stroke="var(--orange)" stroke-width="3.5"/>

    <!-- central ring -->
    <circle cx="600" cy="389" r="142" fill="var(--white)"/>
    <path d="M458 398 A142 142 0 0 1 742 398" fill="none" stroke="var(--orange)" stroke-width="12"/>
    <path d="M458 398 A142 142 0 0 0 742 398" fill="none" stroke="var(--blue)" stroke-width="12"/>

    <!-- orbit nodes -->
    <g fill="var(--white)" stroke="var(--blue)" stroke-width="3">
      <circle cx="440" cy="302" r="8"/>
      <circle cx="417" cy="412" r="8"/>
      <circle cx="458" cy="510" r="8"/>
      <circle cx="548" cy="568" r="8"/>
      <circle cx="653" cy="568" r="8"/>
      <circle cx="739" cy="510" r="8"/>
      <circle cx="781" cy="412" r="8"/>
      <circle cx="759" cy="302" r="8"/>
    </g>
    <g fill="var(--orange)">
      <circle cx="440" cy="302" r="3.6"/>
      <circle cx="417" cy="412" r="3.6"/>
      <circle cx="458" cy="510" r="3.6"/>
      <circle cx="548" cy="568" r="3.6"/>
      <circle cx="653" cy="568" r="3.6"/>
      <circle cx="739" cy="510" r="3.6"/>
      <circle cx="781" cy="412" r="3.6"/>
      <circle cx="759" cy="302" r="3.6"/>
    </g>

    <!-- badge pointers -->
    <polygon points="397,269 407,291 386,302" fill="var(--orange)"/>
    <polygon points="802,269 792,291 813,302" fill="var(--blue)"/>
    <polygon points="364,404 384,417 371,437" fill="var(--blue)"/>
    <polygon points="833,404 813,417 826,437" fill="var(--orange)"/>
    <polygon points="410,534 434,536 431,561" fill="var(--orange)"/>
    <polygon points="787,534 763,536 766,561" fill="var(--blue)"/>
    <polygon points="517,608 539,596 550,618" fill="var(--blue)"/>
    <polygon points="680,608 659,596 648,618" fill="var(--orange)"/>

    <!-- badges -->
    <g fill="var(--white)" stroke-width="9">
      <circle cx="348" cy="270" r="51" stroke="var(--orange)"/>
      <circle cx="321" cy="429" r="51" stroke="var(--blue)"/>
      <circle cx="384" cy="577" r="51" stroke="var(--orange)"/>
      <circle cx="519" cy="658" r="51" stroke="var(--blue)"/>
      <circle cx="679" cy="658" r="51" stroke="var(--orange)"/>
      <circle cx="813" cy="577" r="51" stroke="var(--blue)"/>
      <circle cx="876" cy="429" r="51" stroke="var(--orange)"/>
      <circle cx="852" cy="270" r="51" stroke="var(--blue)"/>
    </g>

    <!-- badge icons -->
    <rect x="326" y="248" width="44" height="44" rx="8" fill="var(--blue)" role="img" aria-label="Icon: two people in conversation"/>
    <rect x="299" y="407" width="44" height="44" rx="8" fill="var(--orange)" role="img" aria-label="Icon: document with protective shield"/>
    <rect x="362" y="555" width="44" height="44" rx="8" fill="var(--blue)" role="img" aria-label="Icon: gear with warning sign"/>
    <rect x="497" y="636" width="44" height="44" rx="8" fill="var(--orange)" role="img" aria-label="Icon: strategy clipboard and pencil"/>
    <rect x="657" y="636" width="44" height="44" rx="8" fill="var(--blue)" role="img" aria-label="Icon: person inside performance ring"/>
    <rect x="791" y="555" width="44" height="44" rx="8" fill="var(--orange)" role="img" aria-label="Icon: hand holding rising chart"/>
    <rect x="854" y="407" width="44" height="44" rx="8" fill="var(--blue)" role="img" aria-label="Icon: money gear with branching funds"/>
    <rect x="830" y="248" width="44" height="44" rx="8" fill="var(--orange)" role="img" aria-label="Icon: calculator and cost report"/>
  </svg>

  <div class="role-title">CHIEF<br>FINANCIAL<br>OFFICER</div>

  <!-- services, left -->
  <div class="service service--left" style="right:948px;top:206px;width:260px;">
    Communication
    <span class="service-detail" style="margin-top:4px;">Board of Directors,<br>creditors, owners,<br>investors, credit<br>rating agencies</span>
  </div>
  <div class="service service--left" style="right:981px;top:388px;width:220px;">
    Compliance
    <span class="service-detail" style="margin-top:4px;">Tax, legal<br>and regulatory</span>
  </div>
  <div class="service service--left" style="right:914px;top:535px;width:220px;">
    Risk<br>Management<br>System
  </div>
  <div class="service service--left" style="right:759px;top:697px;width:220px;">
    Budgeting<br>&amp; Strategic<br>Planning
  </div>

  <!-- services, right -->
  <div class="service service--right" style="left:752px;top:697px;width:240px;">
    Performance<br>Evaluation<br>Programme
  </div>
  <div class="service service--right" style="left:911px;top:535px;width:260px;">
    Long &amp; Short<br>Term Investment<br>Decisions
  </div>
  <div class="service service--right" style="left:977px;top:373px;width:220px;">
    Capital<br>Structure<br>and the<br>Cost of Capital
  </div>
  <div class="service service--right" style="left:948px;top:211px;width:220px;">
    Cost<br>Accounting<br>&amp; Cost<br>Management
  </div>

  <!-- footer -->
  <div class="footer-band">
    <svg class="web-icon" width="18" height="18" viewBox="0 0 18 18" aria-hidden="true">
      <g fill="none" stroke="var(--white)" stroke-width="1.6">
        <circle cx="9" cy="9" r="7.5"/>
        <ellipse cx="9" cy="9" rx="3.2" ry="7.5"/>
        <line x1="1.5" y1="9" x2="16.5" y2="9"/>
      </g>
    </svg>
    <span class="web-address">www.hollinsadvisory.com.au</span>
  </div>
  <div class="footer-accent"></div>

</div>
</body>
</html>
```